Harbor Crest Renewal Business Cards

We need a sleek and sexy business card design

Contact Information for Business Card

Name, address, phone number, email. Martin DeSolva 482 Bramble Court Suite 200C Pinefield NY 11790 (631)584-2276 Also a second version with the name Derek Hollis

```html
<!DOCTYPE html>
<html lang="en">
<head>
<meta charset="utf-8">
<title>Harbor Crest Renewal Business Cards</title>
<link rel="stylesheet" href="https://fonts.googleapis.com/css2?family=Montserrat:wght@600&family=Arimo:wght@400;700&display=swap">
<style>
  :root {
    --page: #1b1d20;
    --card: #2a2b2d;
    --card-light: #333436;
    --accent: #e8541c;
    --icon: #1d5fbf;
    --ink: #ffffff;
    --ink-soft: #d9d9d9;
  }
  * { margin: 0; padding: 0; box-sizing: border-box; }
  html, body { width: 1200px; height: 900px; overflow: hidden; }
  body {
    background: var(--page);
    display: flex;
    flex-direction: column;
    align-items: center;
    justify-content: center;
    gap: 56px;
  }
  .card {
    position: relative;
    width: 640px;
    height: 366px;
    border-radius: 26px;
    background: linear-gradient(135deg, var(--card-light), var(--card) 60%);
    box-shadow: 0 0 0 3px var(--accent), 0 14px 30px rgba(0,0,0,.5);
    overflow: hidden;
  }
  .brand {
    position: absolute;
    display: flex;
    align-items: center;
    gap: 12px;
    font-family: "Montserrat", sans-serif;
    font-weight: 600;
    color: var(--ink);
    letter-spacing: .5px;
    white-space: nowrap;
  }
  .brand-mark {
    width: 22px;
    height: 22px;
    background: var(--accent);
  }
  .front .brand { top: 40px; left: 44px; font-size: 30px; }
  .contact-list {
    position: absolute;
    left: 44px;
    top: 150px;
    list-style: none;
    font-family: "Arimo", sans-serif;
    font-size: 17px;
    color: var(--ink-soft);
  }
  .contact-list li { display: flex; align-items: center; gap: 10px; margin-bottom: 12px; }
  .contact-list svg { width: 14px; height: 14px; fill: var(--icon); flex: none; }
  .holder-name {
    position: absolute;
    right: 44px;
    top: 150px;
    font-family: "Arimo", sans-serif;
    font-weight: 700;
    font-size: 30px;
    letter-spacing: 1px;
    text-transform: uppercase;
    color: var(--ink);
    white-space: nowrap;
  }
  .name-tab {
    position: absolute;
    right: 0;
    top: 150px;
    width: 14px;
    height: 36px;
    background: var(--accent);
  }
  .address {
    position: absolute;
    right: 44px;
    bottom: 40px;
    text-align: right;
    font-family: "Arimo", sans-serif;
    font-style: normal;
    font-size: 18px;
    line-height: 1.4;
    color: var(--ink-soft);
  }
  .back .brand { right: 50px; top: 50%; transform: translateY(-50%); font-size: 38px; }
</style>
</head>
<body>
  <section class="card front">
    <div class="brand"><span class="brand-mark"></span>Harbor Crest Renewal</div>
    <ul class="contact-list">
      <li><svg viewBox="0 0 16 16"><path d="M3 1l3 3-1.5 2a9 9 0 0 0 5.5 5.5L12 10l3 3-2 2C7 15 1 9 1 3z"/></svg>(631)584-2276</li>
      <li><svg viewBox="0 0 16 16"><path d="M1 3h14v10H1zM2 4l6 5 6-5"/></svg>info@harborcrestrenewal.com</li>
      <li><svg viewBox="0 0 16 16"><circle cx="8" cy="8" r="7"/></svg>www.harborcrestrenewal.com</li>
    </ul>
    <div class="holder-name">Derek Hollis</div>
    <span class="name-tab"></span>
    <address class="address">482 Bramble Court<br>Suite 200C<br>Pinefield NY 11790</address>
  </section>
  <section class="card back">
    <div class="brand">Harbor Crest Renewal</div>
  </section>
</body>
</html>
```